Commercial Loan Originator Business Card (CHANGE COLORS SCHEME)

CHANGE COLOR SCHEME - SAME DESIGN

Name Marissa Lantham
Title Commercial Loan Originator
Office (800) 641-2905 x68
Direct (240) 617-2435
Email brightleaf4you@mailpost.example

Name Derek Fallow
Office (800) 641-2905 x70
Direct (410) 932-1864
Email d.falthebroker@mailpost.example

Name Gordon Wexley
Office (800) 641-2905 x71
Direct (215) 346-2081
Email g.wexley37@mailpost.example

Name Lyn Moreau
Office (800) 641-2905 x
Direct (202) 458-1937
Email lmoreau64@mailpost.example

Name Nadia Strand
Office (800) 641-2905 x72
Direct (240) 871-5246
Email qrzhomelending@mailpost.example

```html
<!DOCTYPE html>
<html lang="en">
<head>
<meta charset="UTF-8">
<title>Commercial Loan Originator Business Cards</title>
<link href="https://fonts.googleapis.com/css2?family=Signika:wght@700&family=Fira+Sans+Condensed:wght@400;500&family=Fira+Sans:wght@400&display=swap" rel="stylesheet">
<style>
  :root {
    --page-bg: #ebebeb;
    --text: #ffffff;
    --maroon-dark: #45122b; --maroon-light: #851f50; --maroon-band: #8a2355;
    --slate-dark: #2b3e40; --slate-light: #4d6668; --slate-band: #587476;
    --navy-dark: #0e2149; --navy-light: #22508a; --navy-band: #21508c;
    --plum-dark: #401d57; --plum-light: #6c4087; --plum-band: #73488f;
    --tan-dark: #735c49; --tan-light: #a6927c; --tan-band: #a8937c;
  }
  * { margin: 0; padding: 0; box-sizing: border-box; }
  html, body { width: 1200px; height: 3112px; overflow: hidden; background: var(--page-bg); }
  .card-sheet { position: relative; width: 1200px; height: 3112px; }
  .business-card {
    position: absolute; left: 156px; width: 866px; height: 495px; overflow: hidden;
    box-shadow: 14px 18px 22px rgba(0,0,0,0.28);
    color: var(--text);
  }
  .card-maroon { top: 160px; background: linear-gradient(30deg, var(--maroon-light), var(--maroon-dark) 70%); }
  .card-slate  { top: 742px; background: linear-gradient(30deg, var(--slate-light), var(--slate-dark) 70%); }
  .card-navy   { top: 1323px; background: linear-gradient(30deg, var(--navy-light), var(--navy-dark) 70%); }
  .card-plum   { top: 1905px; background: linear-gradient(30deg, var(--plum-light), var(--plum-dark) 70%); }
  .card-tan    { top: 2486px; background: linear-gradient(30deg, var(--tan-light), var(--tan-dark) 70%); }
  .card-art { position: absolute; inset: 0; width: 100%; height: 100%; }
  .identity { position: absolute; left: 62px; top: 74px; display: inline-block; }
  .person-name {
    font-family: "Signika", sans-serif; font-weight: 700; font-size: 45px; line-height: 1;
    padding-bottom: 4px; border-bottom: 2.5px solid var(--text); white-space: nowrap;
  }
  .job-title {
    font-family: "Fira Sans Condensed", sans-serif; font-weight: 400; font-size: 20.5px;
    letter-spacing: 0.2px; margin-top: 6px; padding-left: 3px; white-space: nowrap;
  }
  .contact-list { position: absolute; left: 62px; top: 294px; list-style: none; }
  .contact-row { display: flex; align-items: baseline; height: 44px; }
  .contact-row.email-row { height: 40px; }
  .contact-label {
    width: 66px; font-family: "Fira Sans Condensed", sans-serif; font-weight: 500; font-size: 15px;
  }
  .contact-value { font-family: "Fira Sans", sans-serif; font-size: 28.5px; white-space: nowrap; }
</style>
</head>
<body>
<main class="card-sheet">

  <section class="business-card card-maroon">
    <svg class="card-art" viewBox="0 0 717 410" preserveAspectRatio="none">
      <defs><linearGradient id="photo-maroon" x1="0" y1="0" x2="0" y2="1"><stop offset="0" stop-color="#f1eeec"/><stop offset="0.55" stop-color="#c98a78"/><stop offset="1" stop-color="#e64fad"/></linearGradient></defs>
      <polygon points="371,0 412,0 543,410 502,410" fill="var(--maroon-band)" opacity="0.85"/>
      <polygon points="384,156 404,156 484,410 464,410" fill="var(--maroon-band)" opacity="0.55"/>
      <polygon points="412,0 717,0 717,410 543,410" fill="url(#photo-maroon)" role="img" aria-label="Portrait photo of Marissa Lantham"/>
    </svg>
    <div class="identity"><h2 class="person-name">Marissa Lantham</h2><p class="job-title">COMMERCIAL LOAN ORIGINATOR</p></div>
    <ul class="contact-list">
      <li class="contact-row"><span class="contact-label">OFFICE</span><span class="contact-value">(800) 641-2905 x68</span></li>
      <li class="contact-row"><span class="contact-label">DIRECT</span><span class="contact-value">(240) 617-2435</span></li>
      <li class="contact-row email-row"><span class="contact-label">EMAIL</span><span class="contact-value">brightleaf4you@mailpost.example</span></li>
    </ul>
  </section>

  <section class="business-card card-slate">
    <svg class="card-art" viewBox="0 0 717 410" preserveAspectRatio="none">
      <defs><linearGradient id="photo-slate" x1="0" y1="0" x2="0" y2="1"><stop offset="0" stop-color="#c9d3da"/><stop offset="0.45" stop-color="#6f8290"/><stop offset="1" stop-color="#2b302e"/></linearGradient></defs>
      <polygon points="371,0 412,0 543,410 502,410" fill="var(--slate-band)" opacity="0.85"/>
      <polygon points="384,156 404,156 484,410 464,410" fill="var(--slate-band)" opacity="0.55"/>
      <polygon points="412,0 717,0 717,410 543,410" fill="url(#photo-slate)" role="img" aria-label="Portrait photo of Derek Fallow"/>
    </svg>
    <div class="identity"><h2 class="person-name">Derek Fallow</h2><p class="job-title">COMMERCIAL LOAN ORIGINATOR</p></div>
    <ul class="contact-list">
      <li class="contact-row"><span class="contact-label">OFFICE</span><span class="contact-value">(800) 641-2905 x70</span></li>
      <li class="contact-row"><span class="contact-label">DIRECT</span><span class="contact-value">(410) 932-1864</span></li>
      <li class="contact-row email-row"><span class="contact-label">EMAIL</span><span class="contact-value">d.falthebroker@mailpost.example</span></li>
    </ul>
  </section>

  <section class="business-card card-navy">
    <svg class="card-art" viewBox="0 0 717 410" preserveAspectRatio="none">
      <defs><linearGradient id="photo-navy" x1="0" y1="0" x2="0" y2="1"><stop offset="0" stop-color="#7f9fbf"/><stop offset="0.5" stop-color="#4a4a58"/><stop offset="1" stop-color="#1a2540"/></linearGradient></defs>
      <polygon points="371,0 412,0 543,410 502,410" fill="var(--navy-band)" opacity="0.85"/>
      <polygon points="384,156 404,156 484,410 464,410" fill="var(--navy-band)" opacity="0.55"/>
      <polygon points="412,0 717,0 717,410 543,410" fill="url(#photo-navy)" role="img" aria-label="Portrait photo of Gordon Wexley"/>
    </svg>
    <div class="identity"><h2 class="person-name">Gordon Wexley</h2><p class="job-title">COMMERCIAL LOAN ORIGINATOR</p></div>
    <ul class="contact-list">
      <li class="contact-row"><span class="contact-label">OFFICE</span><span class="contact-value">(800) 641-2905 x71</span></li>
      <li class="contact-row"><span class="contact-label">DIRECT</span><span class="contact-value">(215) 346-2081</span></li>
      <li class="contact-row email-row"><span class="contact-label">EMAIL</span><span class="contact-value">g.wexley37@mailpost.example</span></li>
    </ul>
  </section>

  <section class="business-card card-plum">
    <svg class="card-art" viewBox="0 0 717 410" preserveAspectRatio="none">
      <defs><linearGradient id="photo-plum" x1="0" y1="0" x2="0" y2="1"><stop offset="0" stop-color="#b65a4c"/><stop offset="0.5" stop-color="#8a5040"/><stop offset="1" stop-color="#4a3a50"/></linearGradient></defs>
      <polygon points="371,0 412,0 543,410 502,410" fill="var(--plum-band)" opacity="0.85"/>
      <polygon points="384,156 404,156 484,410 464,410" fill="var(--plum-band)" opacity="0.55"/>
      <polygon points="412,0 717,0 717,410 543,410" fill="url(#photo-plum)" role="img" aria-label="Portrait photo of Lyn Moreau"/>
    </svg>
    <div class="identity"><h2 class="person-name">Lyn Moreau</h2><p class="job-title">COMMERCIAL LOAN ORIGINATOR</p></div>
    <ul class="contact-list">
      <li class="contact-row"><span class="contact-label">OFFICE</span><span class="contact-value">(800) 641-2905 x</span></li>
      <li class="contact-row"><span class="contact-label">DIRECT</span><span class="contact-value">(202) 458-1937</span></li>
      <li class="contact-row email-row"><span class="contact-label">EMAIL</span><span class="contact-value">lmoreau64@mailpost.example</span></li>
    </ul>
  </section>

  <section class="business-card card-tan">
    <svg class="card-art" viewBox="0 0 717 410" preserveAspectRatio="none">
      <defs><linearGradient id="photo-tan" x1="0" y1="0" x2="0" y2="1"><stop offset="0" stop-color="#d7cbbd"/><stop offset="0.5" stop-color="#8a6a55"/><stop offset="1" stop-color="#2e2826"/></linearGradient></defs>
      <polygon points="371,0 412,0 543,410 502,410" fill="var(--tan-band)" opacity="0.85"/>
      <polygon points="384,156 404,156 484,410 464,410" fill="var(--tan-band)" opacity="0.55"/>
      <polygon points="412,0 717,0 717,410 543,410" fill="url(#photo-tan)" role="img" aria-label="Portrait photo of Nadia Strand"/>
    </svg>
    <div class="identity"><h2 class="person-name">Nadia Strand</h2><p class="job-title">COMMERCIAL LOAN ORIGINATOR</p></div>
    <ul class="contact-list">
      <li class="contact-row"><span class="contact-label">OFFICE</span><span class="contact-value">(800) 641-2905 x72</span></li>
      <li class="contact-row"><span class="contact-label">DIRECT</span><span class="contact-value">(240) 871-5246</span></li>
      <li class="contact-row email-row"><span class="contact-label">EMAIL</span><span class="contact-value">qrzhomelending@mailpost.example</span></li>
    </ul>
  </section>

</main>
</body>
</html>
```